Bluegate Physiotherapy
Business Cards, Stationary, Letterhead, Magnet, Presentation Folder, A5 Referral Pad, Email Signatur
Bluegate Physiotherapy -
Creative Brief
Professional
Tom Ellingsworth
BSc Physiotherapy / Acupuncturist / Cert IV Occupational Health & Safety
Unit 3, 48 Kestrel Lane, Mandurah WA 6210
tom.ellingsworth@bluegatephysio-example.com.au
www.bluegatephysio-example.com.au
Magnet to be standard business card size (portrait OR landscape) and include only phone, address and website (in addition to graphic component). Referral pad to be A5 size. At the TOP: "Patient Name", "Date" as well as 4 tick boxes "W.C.", "Vet. Affairs", "Private" "EPC". At the BOTTOM: "Referring Doctor" "Sign" "Doctors Name" and "Address" as well as "Preferred Contact" with 4 tick boxes "E-mail", "Phone", "Fax", "Snail Mail". Down one SIDE to have a list: "Manual Therapy", "Massage", "Exercise Prescription", "Gym Based Rehab", "Workplace Assessment", "Ergonomics", "Acupuncture", "Sports Physiotherapy", "Womens Health".

```html
<!DOCTYPE html>
<html lang="en">
<head>
<meta charset="utf-8">
<title>Bluegate Physiotherapy – Stationery Set</title>
<link href="https://fonts.googleapis.com/css2?family=Open+Sans:wght@400;700&display=swap" rel="stylesheet">
<style>
:root{
  --bg:#ffffff;
  --paper:#ffffff;
  --edge:#d9dde2;
  --blue:#1f80c6;
  --blue-deep:#0b5b9e;
  --blue-light:#4aa6de;
  --orange:#f39a1e;
  --ink:#333a40;
  --muted:#8a9096;
  --faint:#e7eef5;
}
*{box-sizing:border-box;margin:0;padding:0}
html,body{width:1200px;height:470px;overflow:hidden;background:var(--bg)}
body{font-family:"Open Sans",Arial,sans-serif;color:var(--ink);position:relative}
.piece{position:absolute;background:var(--paper);border:1px solid var(--edge);box-shadow:0 2px 5px rgba(0,0,0,.14);overflow:hidden}
.brand{display:flex;align-items:center;gap:4px;font-weight:700;color:var(--blue);white-space:nowrap;line-height:1}
.brand .dot{display:inline-block;flex:none;border-radius:50%;background:var(--blue)}
.fine{font-size:4px;line-height:1.35;color:var(--muted);white-space:nowrap}

/* business cards */
.card .brand{white-space:normal;line-height:1.15;gap:3px}
.card .fine{font-size:3.4px;white-space:normal}
.card-a{left:24px;top:158px;width:68px;height:40px;padding:6px}
.card-a .brand{font-size:6px}.card-a .dot{width:6px;height:6px}
.card-b{left:96px;top:158px;width:70px;height:40px;padding:5px}
.card-b .name{font-size:5px;font-weight:700;color:var(--ink);margin-bottom:1px}
.card-b .band{position:absolute;left:0;right:0;bottom:0;height:9px;background:linear-gradient(90deg,var(--blue),var(--blue-light))}
.card-c{left:20px;top:218px;width:70px;height:40px;padding:5px;background:linear-gradient(135deg,var(--blue-light),var(--blue-deep));border-color:var(--blue-deep)}
.card-c .fine{color:#fff}
.card-d{left:96px;top:218px;width:70px;height:40px;padding:5px;background:linear-gradient(135deg,#f8b54a,var(--orange));border-color:#e08a12}
.card-d .brand{color:#fff;font-size:5.5px}.card-d .dot{background:#fff;width:5px;height:5px}
.card-e{left:45px;top:264px;width:56px;height:36px;padding:5px 4px}
.card-e .brand{font-size:4.5px}.card-e .dot{width:4.5px;height:4.5px}

/* letterhead */
.letterhead{left:235px;top:19px;width:293px;height:425px;padding:20px 22px}
.letterhead .brand{font-size:12px}.letterhead .dot{width:12px;height:12px}
.watermark{position:absolute;left:50%;top:50%;transform:translate(-50%,-50%);display:flex;flex-direction:column;align-items:center;gap:8px;color:var(--faint);font-weight:700;font-size:14px;white-space:nowrap}
.watermark .ring{width:90px;height:90px;border-radius:50%;background:var(--faint)}
.letterhead .footer{position:absolute;left:22px;bottom:16px}

/* folder */
.folder{left:533px;top:10px;width:336px;height:445px;border:none;background:transparent;box-shadow:0 2px 6px rgba(0,0,0,.16)}
.folder .back{position:absolute;left:0;top:0;width:163px;height:100%;background:linear-gradient(135deg,var(--blue-light) 0%,var(--blue) 45%,var(--blue-deep) 100%)}
.folder .back .fine{position:absolute;left:22px;top:320px;color:#e4f1fb}
.folder .front{position:absolute;left:163px;top:0;width:173px;height:100%;background:var(--paper);border:1px solid var(--edge);border-left:none}
.folder .front .brand{position:absolute;left:16px;top:22px;font-size:10px}
.folder .front .dot{width:10px;height:10px}
.folder .emblem{position:absolute;left:40px;top:150px;width:95px;height:95px;border-radius:50%;background:linear-gradient(135deg,var(--orange),var(--blue))}
.folder .emblem-name{position:absolute;left:0;right:0;top:255px;text-align:center;font-size:8px;font-weight:700;color:var(--blue)}
.folder svg{position:absolute;left:0;bottom:0}

/* compliment slips */
.slip{width:150px;height:18px;padding:3px 5px;display:flex;justify-content:space-between;align-items:center}
.slip .brand{font-size:5px}.slip .dot{width:5px;height:5px}
.slip-1{left:1037px;top:22px}.slip-2{left:1037px;top:43px}.slip-3{left:1037px;top:64px}

/* envelope */
.envelope{left:893px;top:156px;width:295px;height:144px;padding:12px 14px}
.envelope .brand{font-size:9px}.envelope .dot{width:9px;height:9px}
.envelope .footer{position:absolute;left:14px;bottom:10px}
.envelope-flap{position:absolute;left:893px;top:302px;width:295px;height:46px}
</style>
</head>
<body>

<!-- business cards -->
<div class="piece card card-a"><div class="brand"><span class="dot"></span><span>Bluegate Physiotherapy</span></div></div>
<div class="piece card card-b">
  <div class="name">Tom Ellingsworth</div>
  <div class="fine">BSc Physiotherapy / Acupuncturist</div>
  <div class="fine">(08) 9555 0148</div>
  <div class="band"></div>
</div>
<div class="piece card card-c">
  <div class="fine">Unit 3, 48 Kestrel Lane,</div>
  <div class="fine">Mandurah WA 6210</div>
  <div class="fine">(08) 9555 0148</div>
  <div class="fine">www.bluegatephysio-example.com.au</div>
</div>
<div class="piece card card-d"><div class="brand"><span class="dot"></span><span>Bluegate Physiotherapy</span></div></div>
<div class="piece card card-e"><div class="brand"><span class="dot"></span><span>Bluegate Physiotherapy</span></div></div>

<!-- letterhead -->
<div class="piece letterhead">
  <div class="brand"><span class="dot"></span>Bluegate Physiotherapy</div>
  <div class="watermark"><span class="ring"></span>Bluegate Physiotherapy</div>
  <div class="footer">
    <div class="fine">Unit 3, 48 Kestrel Lane, Mandurah WA 6210 · (08) 9555 0148</div>
    <div class="fine">tom.ellingsworth@bluegatephysio-example.com.au · www.bluegatephysio-example.com.au</div>
  </div>
</div>

<!-- presentation folder -->
<div class="piece folder">
  <div class="back">
    <div class="fine">
      Unit 3, 48 Kestrel Lane, Mandurah WA 6210<br>
      tom.ellingsworth@bluegatephysio-example.com.au<br>
      www.bluegatephysio-example.com.au
    </div>
  </div>
  <div class="front">
    <div class="brand"><span class="dot"></span>Bluegate Physiotherapy</div>
    <div class="emblem"></div>
    <div class="emblem-name">Bluegate Physiotherapy</div>
  </div>
  <svg width="336" height="70" viewBox="0 0 336 70">
    <path d="M0 40 Q60 40 80 20 L163 20 L163 70 L0 70 Z" fill="rgba(0,0,0,.12)"/>
    <path d="M163 30 L336 30" stroke="var(--edge)" stroke-width="1"/>
  </svg>
</div>

<!-- compliment slips -->
<div class="piece slip slip-1"><div class="brand"><span class="dot"></span>Bluegate Physiotherapy</div><div class="fine">Mandurah WA 6210</div></div>
<div class="piece slip slip-2"><div class="brand"><span class="dot"></span>Bluegate Physiotherapy</div><div class="fine">Mandurah WA 6210</div></div>
<div class="piece slip slip-3"><div class="brand"><span class="dot"></span>Bluegate Physiotherapy</div><div class="fine">Mandurah WA 6210</div></div>

<!-- envelope -->
<div class="piece envelope">
  <div class="brand"><span class="dot"></span>Bluegate Physiotherapy</div>
  <div class="footer">
    <div class="fine">Unit 3, 48 Kestrel Lane, Mandurah WA 6210</div>
    <div class="fine">www.bluegatephysio-example.com.au</div>
  </div>
</div>
<svg class="envelope-flap" viewBox="0 0 295 46">
  <path d="M0 0 L295 0 L250 42 Q147 48 45 42 Z" fill="#f6f7f8" stroke="var(--edge)"/>
</svg>

</body>
</html>
```